M Zyvantics Buisness Cards

I need a technology focused clean business card for my employees. I have attached out logo to include in the mocks. We're a modern tech consulting firm that drives to interface humanity with technology in a truly cohesive fashion.

```html
<!DOCTYPE html>
<html lang="en">
<head>
<meta charset="utf-8">
<title>M Zyvantics Business Cards</title>
<link href="https://fonts.googleapis.com/css2?family=Open+Sans:wght@400;700&display=swap" rel="stylesheet">
<style>
  :root {
    --canvas: #3d342e;
    --blue-light: #1a72bb;
    --blue-dark: #063b6b;
    --brand-blue: #1a6fb5;
    --brand-grey: #8a8c8e;
    --text-grey: #555a5f;
    --paper: #ffffff;
    --tint: #e6f0f8;
  }
  * { box-sizing: border-box; margin: 0; padding: 0; }
  html, body { width: 1200px; height: 1200px; overflow: hidden; }
  body {
    background: var(--canvas);
    font-family: "Open Sans", sans-serif;
    display: flex;
    flex-direction: column;
    align-items: center;
    justify-content: center;
    gap: 60px;
  }
  .card {
    width: 880px;
    height: 503px;
    position: relative;
    overflow: hidden;
    box-shadow: 0 10px 30px rgba(0,0,0,0.35);
  }
  .card-front {
    background: linear-gradient(120deg, var(--blue-light) 0%, var(--blue-dark) 100%);
    display: flex;
    align-items: center;
    justify-content: center;
  }
  .brand {
    display: flex;
    align-items: center;
    gap: 16px;
    font-weight: 700;
    font-size: 58px;
    letter-spacing: 1px;
    color: var(--brand-grey);
  }
  .brand-dot {
    width: 40px; height: 40px;
    border-radius: 50%;
    background: var(--brand-grey);
  }
  .card-back { background: var(--paper); }
  .back-decor {
    position: absolute;
    width: 420px; height: 420px;
    border-radius: 50%;
    background: var(--tint);
    right: -150px; top: 150px;
  }
  .card-back .brand {
    position: absolute;
    left: 70px; top: 50%;
    transform: translateY(-50%);
    font-size: 46px;
    color: var(--brand-blue);
  }
  .card-back .brand-dot { width: 32px; height: 32px; background: var(--brand-blue); }
  .divider {
    position: absolute;
    left: 475px; top: 120px;
    width: 2px; height: 270px;
    background: var(--brand-blue);
    opacity: 0.6;
  }
  .contact {
    position: absolute;
    left: 505px; top: 115px;
    color: var(--text-grey);
    z-index: 1;
  }
  .contact-name {
    font-size: 30px; font-weight: 700;
    color: var(--brand-blue);
    letter-spacing: -0.5px;
    line-height: 1.1;
  }
  .contact-role { font-size: 19px; margin-bottom: 22px; }
  .contact-list { list-style: none; font-size: 18px; line-height: 1.45; }
  .contact-list li { display: flex; align-items: flex-start; gap: 10px; }
  .contact-list li.address { margin-bottom: 14px; }
  .icon { width: 20px; height: 20px; flex: none; margin-top: 4px; }
</style>
</head>
<body>
  <section class="card card-front">
    <div class="brand"><span class="brand-dot"></span>M Zyvantics</div>
  </section>

  <section class="card card-back">
    <div class="back-decor"></div>
    <div class="brand"><span class="brand-dot"></span>M Zyvantics</div>
    <div class="divider"></div>
    <div class="contact">
      <p class="contact-name">JOHN DOE</p>
      <p class="contact-role">Director</p>
      <ul class="contact-list">
        <li class="address">
          <svg class="icon" viewBox="0 0 20 20"><circle cx="10" cy="10" r="9" fill="none" stroke="#1a6fb5" stroke-width="1.5"/><path d="M10 4.5a3.5 3.5 0 0 0-3.5 3.5c0 2.6 3.5 7 3.5 7s3.5-4.4 3.5-7A3.5 3.5 0 0 0 10 4.5z" fill="#1a6fb5"/><circle cx="10" cy="8" r="1.3" fill="#fff"/></svg>
          <span>Dummy city<br>Dummy Country Land</span>
        </li>
        <li>
          <svg class="icon" viewBox="0 0 20 20"><circle cx="10" cy="10" r="9" fill="none" stroke="#1a6fb5" stroke-width="1.5"/><path d="M6 7c0 4 3 7 7 7l1-2-2-1-1 1c-1.5-.5-2.5-1.5-3-3l1-1-1-2z" fill="#1a6fb5"/></svg>
          <span>1-234-567890</span>
        </li>
        <li>
          <svg class="icon" viewBox="0 0 20 20"><circle cx="10" cy="10" r="9" fill="none" stroke="#1a6fb5" stroke-width="1.5"/><circle cx="10" cy="10" r="5" fill="none" stroke="#1a6fb5" stroke-width="1.2"/><path d="M5 10h10M10 5c-2 3-2 7 0 10M10 5c2 3 2 7 0 10" fill="none" stroke="#1a6fb5" stroke-width="1"/></svg>
          <span>www.mzyvantics.com</span>
        </li>
        <li>
          <svg class="icon" viewBox="0 0 20 20"><circle cx="10" cy="10" r="9" fill="none" stroke="#1a6fb5" stroke-width="1.5"/><rect x="5" y="6.5" width="10" height="7" fill="#1a6fb5"/><path d="M5 6.5l5 4 5-4" fill="none" stroke="#fff" stroke-width="1"/></svg>
          <span>john@mzyvantics.com</span>
        </li>
      </ul>
    </div>
  </section>
</body>
</html>
```